KTR Engineering Business Card Design

We’re looking for an elegant, clean, and timeless business card design that communicates experience, capability, and reliability.

KTR Engineering was established in 1995 , we are a Government Contracting company providing Professional Services to the Ministry of Harbor Works, Frontier Stewardship and the Waypoint Consortium. Our capabilities include: Acquisition & Program Management; Intelligence & Security Operations; Cyber, IT & Network Operations; Lifecycle Logistics & Asset Readiness; C5ISR Systems Engineering & Sustainment.

We want the card to reflect a straightforward, confident approach to business. The design should feel polished and professional without being flashy or overly corporate.

Design Direction
Clean, sophisticated, and uncluttered
Elegant but understated
Strong typography and thoughtful spacing
A timeless aesthetic rather than something overly trendy
Confident and established, with a sense of substance
Easy to read and practical in a real-world business setting

The overall impression should be: “These are experienced professionals who know what they’re doing, do what they say, and can be relied upon.”

We’re open to creative interpretations. The finished card should feel distinctive through its typography, proportions, layout, and attention to detail rather than through excessive graphics or visual effects.

We’re looking for a design that would make a potential client immediately feel that they’re dealing with a capable, trustworthy, and established company.

Company Colors: Navy and Gold/Yellow (but you do not need to use these colors on the card)
Company Name: KTR Engineering Associates, Inc. (known as KTR Engineering)
Website: ktrengineering.example
Company Logo: Navy & Gold (other variations attached)

```html
<!DOCTYPE html>
<html lang="en">
<head>
<meta charset="utf-8">
<title>KTR Engineering Business Card</title>
<link href="https://fonts.googleapis.com/css2?family=Montserrat:wght@400;500;700;800&display=swap" rel="stylesheet">
<style>
  :root {
    --navy: #1c2460;
    --navy-deep: #161d52;
    --navy-soft: #2a3478;
    --gold: #f7df4c;
    --white: #ffffff;
    --ink: #2b2b36;
    --stage: #1b1b1d;
  }
  * { margin: 0; padding: 0; box-sizing: border-box; }
  html, body {
    width: 1200px; height: 900px; overflow: hidden;
    background: var(--stage);
    font-family: "Montserrat", sans-serif;
  }
  .canvas { position: relative; width: 1200px; height: 900px; }

  .card {
    position: absolute;
    width: 540px; height: 310px;
    border-radius: 22px;
    overflow: hidden;
  }

  /* Back side */
  .card-back {
    left: 70px; top: 110px;
    background: var(--navy);
    display: flex; align-items: center; justify-content: center;
  }
  .card-back .wordmark {
    font-weight: 800; font-size: 112px; letter-spacing: -2px;
    color: var(--navy-soft);
    line-height: 1;
  }

  /* Front side */
  .card-front {
    left: 590px; top: 480px;
    background: var(--white);
    color: var(--ink);
  }
  .front-logo {
    position: absolute; right: 50px; top: 38px;
    display: flex; align-items: center; gap: 12px;
  }
  .front-logo .dot {
    width: 18px; height: 18px; border-radius: 50%;
    background: var(--gold);
  }
  .front-logo .wordmark {
    font-weight: 800; font-size: 64px; letter-spacing: -1px;
    color: var(--navy); line-height: 1;
  }
  .divider {
    position: absolute; left: 235px; right: 30px; top: 150px;
    height: 1.5px; background: var(--gold);
  }
  .identity {
    position: absolute; left: 38px; top: 130px;
  }
  .identity .name {
    font-weight: 800; font-size: 20px; color: var(--navy);
    letter-spacing: 0.5px; text-transform: uppercase;
  }
  .identity .title {
    font-weight: 500; font-size: 16px; color: #e9c82a;
    margin-top: 2px;
  }
  .contacts {
    position: absolute; left: 38px; top: 195px;
    list-style: none;
    font-size: 15px; color: var(--ink);
  }
  .contacts li {
    display: flex; align-items: center; gap: 10px;
    line-height: 22px;
  }
  .contacts svg { width: 13px; height: 13px; fill: var(--navy); flex: none; }
  .address {
    position: absolute; right: 32px; top: 165px;
    text-align: right; font-size: 14.5px; line-height: 20px;
    color: var(--ink);
  }
  .band { position: absolute; left: 0; bottom: 0; width: 540px; height: 28px; }
</style>
</head>
<body>
<main class="canvas">

  <section class="card card-back" aria-label="Card back">
    <span class="wordmark">KTR</span>
  </section>

  <section class="card card-front" aria-label="Card front">
    <div class="front-logo">
      <span class="dot"></span>
      <span class="wordmark">KTR</span>
    </div>

    <div class="divider"></div>

    <div class="identity">
      <p class="name">Rowan Tessler</p>
      <p class="title">Founder &amp; CEO</p>
    </div>

    <ul class="contacts">
      <li>
        <svg viewBox="0 0 16 16" aria-hidden="true"><path d="M3.5 1l2.5 3-1.5 1.5c.8 2 2.5 3.7 4.5 4.5L10.5 8.5l3 2.5-1.5 3C7 14 2 9 2 2.5z"/></svg>
        555-014-2277
      </li>
      <li>
        <svg viewBox="0 0 16 16" aria-hidden="true"><path d="M1 3h14v10H1zM2 4l6 5 6-5v1L8 10 2 5z" fill-rule="evenodd"/></svg>
        info@ktrengineering.example
      </li>
      <li>
        <svg viewBox="0 0 16 16" aria-hidden="true"><circle cx="8" cy="8" r="7"/></svg>
        info@ktrengineering.example
      </li>
    </ul>

    <address class="address" style="font-style:normal">
      1840 Harbor Crest Road,<br>
      Suite 310, Eastport,<br>
      VA 20190
    </address>

    <svg class="band" viewBox="0 0 540 28" preserveAspectRatio="none" aria-hidden="true">
      <polygon points="0,14 390,0 378,28 0,28" fill="var(--navy)"/>
      <polygon points="396,0 540,0 540,28 384,28" fill="var(--gold)"/>
    </svg>
  </section>

</main>
</body>
</html>
```